TembaLinkHub

Hey

I am involved with crowd funding, please look at one of my current sites www.fundvessel.net
Work is currently under way with a new site www.tembalinkhub.com .wehave the basics but I am not happy with what we have so far. I need to redesign the web site but keep the concept . The cartoon pitch will be kept , along with some of the other functions which we can help you with, unless you are able to build / design something better. I liked a lot of the designs submitted for a previous crowd funning design, far better than what I currently have. To be included on this site will be links to numerous crowd funding sites which I have registered but each site will be focused on a specific topic which will be disclosed once this site is active. I intend to build all these sites through this site. Along with these sites will be a logo design for each site so plenty of work going forward. I have a logo for tembalinkhub already but am open for improvements and suggestions but would like to keep a map or logo of Africa included in the design. To bear in mind this is a African focused buisness which aims to help communities, employment creation, poverty alleviation and help young entrepreneurs kickstarter their buisness . I already have a group logo , which was designed on this site ( look at ubuntu harvests competition) , I would like this logo to be used on all the site so customers and investors link the group and concept togeather. Here is the link http://www.sketchbazaar.example/project-progress.aspx?briefId=48213 . I have removed the ubuntuharvest from the bottom of the logo and will just be using the figurines as the group logo on all web sites. There will be at least fifty related crowd fund projects linked to this site.
If any body has any questions or ideas please feel free to ask for anything you may need. Thanks to everybody who helps with this project. Warmly. Owen

Hi everyone working on my design.

The contact details to use on the site are

27 Velden Close
Kelwater
Cape Town 
+263719483025
+447500294318

E mail enquiries@TembaLinkHub.example

There are two logos, one is the tembalinkhub logo and the other is my group logo which I will attach to the pitch
Good luck and thank you to everybody who is working on this web design
Warmly

Owen

```html
<!DOCTYPE html>
<html lang="en">
<head>
<meta charset="utf-8">
<title>TembaLinkHub – Equity Crowdfunding</title>
<link href="https://fonts.googleapis.com/css2?family=Montserrat:wght@400;500;600;700&family=Raleway:wght@300;400;500&display=swap" rel="stylesheet">
<style>
:root{
  --ink:#333;
  --muted:#8a8a8a;
  --blue:#2a7fc4;
  --blue-deep:#1f6fb8;
  --green:#3f9a3e;
  --orange:#e2562a;
  --slate:#5b7993;
  --tan:#b9a595;
  --steel:#8ea4ba;
  --band:#aaa69d;
  --foot:#ececec;
  --badge:#d6d6d6;
}
*{box-sizing:border-box;margin:0;padding:0}
html,body{width:711px;height:1200px;overflow:hidden;background:#fff}
body{position:relative;font-family:"Montserrat",sans-serif;color:var(--ink)}
.abs{position:absolute}
a{color:inherit;text-decoration:none}

/* top bar */
.top-nav{left:83px;top:8px;font-size:7.6px;font-weight:500;letter-spacing:.2px;display:flex;gap:5px;color:#222}
.top-nav span.sep{color:#999}
.login-badge{left:394px;top:4px;width:22px;height:22px;border-radius:50%;background:#fff;border:2px solid #c8dbe9}
.login-label{left:433px;top:8px;font-size:11px;font-weight:500}
.field{top:7px;height:16px;border:1px solid #d5d5d5;background:#fff;font-size:7px;color:#999;padding:3px 4px}
.go{left:603px;top:6px;width:18px;height:18px;background:var(--blue-deep);border-radius:2px}
.login-links{top:34px;font-size:7px;color:var(--blue)}
.header-rule{left:0;top:28px;width:711px;height:1px;background:#f1f1f1}

.brand{left:85px;top:52px;width:163px;height:42px;display:flex;align-items:center;gap:6px}
.brand .mark{width:22px;height:22px;border-radius:50%;background:var(--blue)}
.brand .name{font-size:15px;font-weight:700;color:var(--blue-deep);letter-spacing:.2px}
.rules{left:296px;top:51px;width:336px;font-size:6.3px;line-height:9px;color:#9a9a9a}

.tabs{left:280px;top:88px;width:350px;height:25px}
.tab-label{top:95px;font-size:10px;font-weight:500;color:#fff;text-align:center}
.header-base{left:0;top:112px;width:711px;height:3px;background:#d9d9d9}

/* hero */
.hero{left:0;top:115px;width:711px;height:273px;background:linear-gradient(180deg,#f3822b 0%,#e9601f 100%)}
.hero-main{left:83px;top:120px;width:545px;height:209px;background:linear-gradient(180deg,#f07a1d 0%,#f9a325 55%,#3a1c0c 80%,#120805 100%)}
.hero-side{top:270px;width:83px;height:117px;background:linear-gradient(180deg,#f5a52a 0%,#e4601d 55%,#1a0b05 100%)}
.promo{top:329px;width:272px;height:58px;display:flex}
.promo .thumb{width:88px;height:58px;background:linear-gradient(180deg,#d8852d,#4a2510);display:flex;align-items:center;justify-content:center;font-family:"Raleway",serif;font-size:22px;font-weight:500;color:#f1e6d6;letter-spacing:1px}
.promo p{flex:1;padding:11px 10px 0 6px;font-size:6.9px;line-height:9.5px;color:#fff}
.promo.fund{left:83px;background:var(--blue)}
.promo.join{left:356px;background:var(--orange)}

/* welcome */
.welcome{left:89px;top:409px;font-family:"Raleway",sans-serif;font-size:17px;font-weight:400;color:#333;line-height:20px}
.welcome strong{display:block;font-weight:500;color:var(--blue-deep);font-size:17.5px}
.what{left:89px;top:471px;font-family:"Raleway",sans-serif;font-size:17px;font-weight:400;color:#333}
.intro{left:89px;top:494px;width:310px;font-size:8.9px;line-height:14.6px;color:#444}

.video-frame{left:410px;top:407px;width:200px;height:139px;background:#fff;border-radius:6px;box-shadow:0 6px 12px rgba(0,0,0,.18),0 0 0 1px #e6e6e6}
.video{left:422px;top:418px;width:178px;height:116px;background:linear-gradient(180deg,#c7c7c4,#9e9d98)}
.video-controls{left:422px;top:518px;width:178px;height:16px;background:#1b1b1b}

/* categories */
.cat-head{left:83px;top:581px;width:124px;height:42px;background:var(--slate);color:#fff;font-family:"Raleway",sans-serif;text-align:center;padding-top:8px;line-height:13px}
.cat-head .light{font-size:13px;font-weight:300;color:#e3ebf2}
.cat-head .bold{font-size:15.5px;font-weight:400}
.cat-list{left:83px;top:627px;width:124px;list-style:none;border:1px solid #ececec;border-top:0}
.cat-list li{font-size:6.6px;color:var(--blue);padding:5px 9px 5px;border-top:1px solid #ececec;line-height:8px}

/* project cards */
.card{width:127px;height:220px;border:1px solid #e6e6e6;background:#fff}
.card .photo{position:absolute;left:1px;top:1px;width:123px;height:74px;background:radial-gradient(circle at 50% 55%,#b8c6d4 0%,#9aa9a8 30%,#3b5a2a 70%,#23381a 100%)}
.card h3{position:absolute;left:6px;top:81px;font-size:9.2px;font-weight:500;color:#222}
.card p{position:absolute;left:6px;top:98px;width:112px;font-size:6.5px;line-height:10.2px;color:#8d8d8d}
.card .stats{position:absolute;left:0;top:164px;width:125px;height:35px;border-top:1px solid #eee}
.card .badge{position:absolute;left:7px;top:6px;width:23px;height:23px;border-radius:50%;background:#e6eef5;border:1px solid #c9d6e3}
.card .lbl{position:absolute;top:7px;font-size:7px;font-weight:700}
.card .amt{position:absolute;top:19px;font-size:10px;font-weight:700}
.card .place{position:absolute;left:0;bottom:0;width:125px;height:18px;background:var(--green);color:#fff;font-size:8.5px;font-weight:600;text-align:center;line-height:18px}

.ad{left:500px;width:127px;height:221px;color:#fff;font-family:"Raleway",sans-serif;font-size:15.5px;font-weight:300;text-align:center;display:flex;align-items:center;justify-content:center;line-height:19px}

/* footer */
.cta{left:78px;top:1059px;width:555px;height:59px;background:var(--band)}
.cta-text{left:96px;top:1069px;font-family:"Raleway",sans-serif;font-size:18.5px;font-weight:300;color:#fff;line-height:19px;letter-spacing:.6px}
.foot{left:78px;top:1118px;width:555px;height:59px;background:var(--foot)}
.foot-nav{left:85px;top:1139px;font-size:10px;color:#666;display:flex;gap:7px}
.foot-nav .sep{color:#bbb}
.trust-badge{top:1132px;height:26px;background:var(--badge);border-radius:3px}
.copy{left:85px;top:1183px;font-size:6.6px;color:#777}
.legal{right:85px;top:1183px;font-size:6.6px;color:#777}
</style>
</head>
<body>

<!-- top bar -->
<nav class="abs top-nav">
  <a>BLOG</a><span class="sep">/</span><a>IPO'S</a><span class="sep">/</span><a>HOW IT WORKS</a><span class="sep">/</span><a>ABOUT</a><span class="sep">/</span><a>MY ACCOUNT</a><span class="sep">/</span><a>MY CART</a>
</nav>
<div class="abs header-rule"></div>
<div class="abs login-badge"></div>
<div class="abs login-label">Login</div>
<div class="abs field" style="left:469px;width:61px">Username</div>
<div class="abs field" style="left:536px;width:62px">••••••</div>
<div class="abs go">
  <svg width="18" height="18" viewBox="0 0 18 18"><path d="M7 5l4 4-4 4" fill="none" stroke="#fff" stroke-width="2"/></svg>
</div>
<div class="abs login-links" style="left:421px">Sign in with Chatterly</div>
<div class="abs login-links" style="left:514px">Register &nbsp;|&nbsp; Forgotten Password</div>

<div class="abs brand"><span class="mark"></span><span class="name">TEMBALINKHUB</span></div>
<p class="abs rules">Ground rules are simple; JOIN, send us a ClipWave or any other video link to any idea. It can be an idea just floating around or an idea which has already come to life. No catches, no entry fee, no award collection fee, only one entry per member.</p>

<svg class="abs tabs" viewBox="0 0 350 25">
  <path d="M3 25 L8 4 Q9 0 13 0 H90 Q94 0 95 4 L100 25Z" fill="var(--blue-deep)"/>
  <path d="M105 25 L110 4 Q111 0 115 0 H203 Q207 0 208 4 L213 25Z" fill="var(--green)"/>
  <path d="M220 25 L225 4 Q226 0 230 0 H336 Q340 0 341 4 L346 25Z" fill="var(--orange)"/>
</svg>
<div class="abs tab-label" style="left:283px;width:97px">Join Now</div>
<div class="abs tab-label" style="left:385px;width:108px">How it works?</div>
<div class="abs tab-label" style="left:500px;width:126px">Browse Companies</div>
<div class="abs header-base"></div>

<!-- hero -->
<section class="abs hero"></section>
<div class="abs hero-side" style="left:0" role="img" aria-label="Savanna sunset with elephant silhouettes"></div>
<div class="abs hero-side" style="left:628px" role="img" aria-label="Savanna sunset with acacia tree silhouettes"></div>
<div class="abs hero-main" role="img" aria-label="African savanna at sunset with acacia tree, giraffe, elephant and rhino silhouettes"></div>

<div class="abs promo fund">
  <div class="thumb" role="img" aria-label="Savanna scene behind the word Fund">FUND</div>
  <p>The elephant with no trunk. They say that a picture paints a thousand words, but no words can describe the pain, the anguish and the... »</p>
</div>
<div class="abs promo join">
  <div class="thumb" role="img" aria-label="Savanna scene behind the word Join">JOIN</div>
  <p>The elephant with no trunk. They say that a picture paints a thousand words, but no words can describe the pain, the anguish and the... »</p>
</div>

<!-- welcome -->
<h1 class="abs welcome">Welcome to<strong>Africa's leading crowdfunding site</strong></h1>
<h2 class="abs what">What is Crowdfunding?</h2>
<p class="abs intro">Crowdfunding enables people to raise money for innovative new projects by getting like-minded individuals to pool their money to back the idea, person or business. It's a way to make things happen.</p>

<div class="abs video-frame"></div>
<div class="abs video" role="img" aria-label="Animated pitch video still"></div>
<svg class="abs" style="left:496px;top:451px" width="32" height="32" viewBox="0 0 32 32">
  <rect x="0.5" y="0.5" width="31" height="31" rx="4" fill="#2a2a2a" stroke="#777"/>
  <path d="M12 9 L23 16 L12 23Z" fill="#fff"/>
</svg>
<svg class="abs" style="left:561px;top:424px" width="34" height="32" viewBox="0 0 34 32">
  <rect width="34" height="32" rx="4" fill="#2a2a2a"/>
  <circle cx="11" cy="13" r="2.5" fill="#fff"/><circle cx="22" cy="8" r="2.5" fill="#fff"/><circle cx="22" cy="18" r="2.5" fill="#fff"/>
  <path d="M11 13 L22 8 M11 13 L22 18" stroke="#fff" stroke-width="1.2"/>
  <text x="17" y="28" font-size="6" fill="#fff" text-anchor="middle" font-family="Montserrat,sans-serif">share</text>
</svg>
<div class="abs video-controls">
  <svg width="178" height="16" viewBox="0 0 178 16">
    <path d="M6 5 L11 8 L6 11Z" fill="#fff"/>
    <text x="18" y="10.5" font-size="5.5" fill="#fff" font-family="Montserrat,sans-serif">00:37</text>
    <rect x="40" y="7" width="84" height="2" fill="#666"/><rect x="40" y="7" width="22" height="2" fill="#fff"/>
    <text x="130" y="10.5" font-size="5.5" fill="#fff" font-family="Montserrat,sans-serif">02:05</text>
    <path d="M152 6 h2 l3 -2 v8 l-3 -2 h-2z" fill="#fff"/>
    <path d="M166 5 l5 6 M171 5 l-5 6" stroke="#fff" stroke-width="1"/>
  </svg>
</div>

<!-- categories -->
<div class="abs cat-head"><div class="light">Business</div><div class="bold">Categories</div></div>
<ul class="abs cat-list">
  <li>COMICS</li><li>ENVIRONMENT</li><li>FASHION</li><li>FILM AND VIDEO</li><li>GAMING</li><li>HEALTH AND FITNESS</li><li>INTERNET, IT AND<br>TELECOMMUNICATIONS</li><li>LEISURE AND TOURISM</li><li>MUSIC</li><li>PROFESSIONAL SERVICES</li><li>TECHNOLOGY</li>
</ul>

<!-- project cards -->
<article class="abs card" style="left:223px;top:581px">
  <div class="photo" role="img" aria-label="Pale blue hydrangea flower"></div>
  <h3>Ut placerat nunc suscipit</h3>
  <p>Ut placerat nunc suscipit metus lacinia vel interdum tortor eleifend. Aliquam erat volutpat. Ut consectetur auctor ornare. Donec molestie eros id lacus porta tempus. Phasellus... »</p>
  <div class="stats"><span class="badge"></span><span class="lbl" style="left:41px;color:var(--blue)">FUNDED</span><span class="amt" style="left:41px;color:#555">$0</span><span class="lbl" style="left:84px;color:var(--orange)">GOAL</span><span class="amt" style="left:84px">$1,000</span></div>
  <div class="place">Russia</div>
</article>
<article class="abs card" style="left:362px;top:581px">
  <div class="photo" role="img" aria-label="Pale blue hydrangea flower"></div>
  <h3>Ut placerat nunc suscipit</h3>
  <p>Ut placerat nunc suscipit metus lacinia vel interdum tortor eleifend. Aliquam erat volutpat. Ut consectetur auctor ornare. Donec molestie eros id lacus porta tempus. Phasellus... »</p>
  <div class="stats"><span class="badge"></span><span class="lbl" style="left:41px;color:var(--blue)">FUNDED</span><span class="amt" style="left:41px;color:#555">$0</span><span class="lbl" style="left:84px;color:var(--orange)">GOAL</span><span class="amt" style="left:84px">$1,000</span></div>
  <div class="place">Russia</div>
</article>
<article class="abs card" style="left:223px;top:814px">
  <div class="photo" role="img" aria-label="Pale blue hydrangea flower"></div>
  <h3>Ut placerat nunc suscipit</h3>
  <p>Ut placerat nunc suscipit metus lacinia vel interdum tortor eleifend. Aliquam erat volutpat. Ut consectetur auctor ornare. Donec molestie eros id lacus porta tempus. Phasellus... »</p>
  <div class="stats"><span class="badge"></span><span class="lbl" style="left:41px;color:var(--blue)">FUNDED</span><span class="amt" style="left:41px;color:#555">$0</span><span class="lbl" style="left:84px;color:var(--orange)">GOAL</span><span class="amt" style="left:84px">$1,000</span></div>
  <div class="place">Russia</div>
</article>
<article class="abs card" style="left:362px;top:814px">
  <div class="photo" role="img" aria-label="Pale blue hydrangea flower"></div>
  <h3>Ut placerat nunc suscipit</h3>
  <p>Ut placerat nunc suscipit metus lacinia vel interdum tortor eleifend. Aliquam erat volutpat. Ut consectetur auctor ornare. Donec molestie eros id lacus porta tempus. Phasellus... »</p>
  <div class="stats"><span class="badge"></span><span class="lbl" style="left:41px;color:var(--blue)">FUNDED</span><span class="amt" style="left:41px;color:#555">$0</span><span class="lbl" style="left:84px;color:var(--orange)">GOAL</span><span class="amt" style="left:84px">$1,000</span></div>
  <div class="place">Russia</div>
</article>

<div class="abs ad" style="top:581px;background:var(--tan)">Advantage<br>Here</div>
<div class="abs ad" style="top:813px;background:var(--steel)">Advantage<br>Here</div>

<!-- footer -->
<div class="abs cta"></div>
<div class="abs cta-text">WOULD YOU LIKE TO KNOW<br>MORE@HUBCIRCLE.EXAMPLE?</div>
<svg class="abs" style="left:442px;top:1073px" width="176" height="32" viewBox="0 0 176 32">
  <circle cx="16" cy="16" r="15" fill="#fff"/>
  <circle cx="52" cy="16" r="15" fill="#fff"/>
  <circle cx="88" cy="16" r="15" fill="#fff"/>
  <circle cx="124" cy="16" r="15" fill="#fff"/>
  <circle cx="119" cy="16" r="2.4" fill="var(--band)"/><circle cx="129" cy="11" r="2.4" fill="var(--band)"/><circle cx="129" cy="21" r="2.4" fill="var(--band)"/>
  <path d="M119 16 L129 11 M119 16 L129 21" stroke="var(--band)" stroke-width="1.4"/>
  <circle cx="160" cy="16" r="15" fill="#fff"/>
  <rect x="152" y="11" width="16" height="11" rx="1.5" fill="var(--band)"/>
  <path d="M152.5 11.5 L160 17.5 L167.5 11.5" fill="none" stroke="#fff" stroke-width="1.3"/>
</svg>

<div class="abs foot"></div>
<nav class="abs foot-nav"><a>JOIN NOW</a><span class="sep">|</span><a>HOW IT WORKS ?</a><span class="sep">|</span><a>BROWSE COMPANIES</a></nav>
<div class="abs trust-badge" style="left:389px;width:101px" role="img" aria-label="Crowdfunding platform accreditation badge"></div>
<div class="abs trust-badge" style="left:499px;width:52px" role="img" aria-label="Security certification badge"></div>
<div class="abs trust-badge" style="left:561px;width:68px" role="img" aria-label="Privacy certification badge"></div>
<div class="abs copy">Copyright 2012 TembaLinkHub</div>
<div class="abs legal">TERMS AND CONDITIONS &nbsp;|&nbsp; PRIVACY POLICY</div>

</body>
</html>
```